依頼概要
■ 依頼の目的/概要

移動販売車の脇に設置するのぼりになります。

■ デザインへの要望

地元の主要農産物(米)をつかっていることを強くアピールし、地域活性につながるような商品(特産品)にしたいです。
商品名は、『アオナギクレープ』・・・「アオナギ」とは、岐阜地方で主に栽培されいてる米の銘柄で、実際美味しいです。
県外での『アオナギ』の認知度を上げることと『アオナギの生産者』に知ってもらうことが目的なので、メインワードを強調したシンプルなデザインを希望します。
現段階でのイメージは、筆書体かなと思っています。

添付①のテンプレートを使用して、作成してください。(当方、イラストレーター未所持ですので、実際開けるのか確認できません。開けない場合は、お手数ですが、下記のサイトから、ダウンロードをお願いいたします。)
http://www.kazaori-hanpu.com/original/download.php

また、添付②のロゴマークも組み込んでください。

■店の情報
アオナギの米粉クレープとタピオカドリンクを可愛いルメトバスで販売しています。
販売場所は、サービスエリア、イベント会場、店舗の駐車場などです。
メイン客層は、女子高校生・大学生などですが、『アオナギの生産者』である年配の方々にも興味をもっていただきたいです。

参考資料として、実際の車両の画像(添付③)を載せます。あわせて、ご確認下さい。

★キーワード★
メイン(必須) アオナギクレープ
サブ(必須)  岐阜(県)〔ぎふ(けん)〕
輪之内(町)〔わのうち(ちょう)〕
ロゴマーク

※キーワードの地名は、漢字でも、ひらがなでも構いません。以前は、『岐阜わのうち』で自作したものを使用していました。

■輪之内町の情報
輪之内町は、岐阜県のこの辺りです。添付④確認

■ のぼりの情報

サイズ:横600×縦1800

■ 納品ファイルの希望

イラストレーター形式

■ 進め方

弊社の希望するイメージに近い提案を1つ(場合によって複数)選択させて頂きます。希望に近づけるために、修正要望を個別にさせて頂くこともあります。コンペ方式のため、修正後に当選されない場合も、どうかご了承ください。

■ その他/注意点

選択させて頂いたデザインの著作権(財産権)等の扱いはTaskora利用規約に従い、弊社に譲渡をお願いします。フォントや画像素材などを利用する場合は上記利用用途に使用できることを確認し、第三者の知的財産権等に注意して下さい。
皆様、たくさんの提案ありがとうございます。
すべてと言っていいほどの提案が、イメージ通りの素晴らしい提案です。
ありがとうございます。

今後の修正依頼は、選定後にさせて頂きたく思います。

まだまだ、いろいろな筆文字やデザインを拝見したいと思っております。
引き続きご提案のほど、お願いいたします。

なお、選定は役場(役所)の人や、友人からもっとも支持があったものを選びたいと思います。
残りわずかではございますが、最後までよろしくお願いいたします。
■ 選んだ理由

もっとも支持を集めた提案に決めさせていただきました。
個人的にも、かわいらしさ、バランスの良さが気に入りました。

■ 提案者全員のお礼・コメント

たくさんの提案をしていただき、本当にありがとうございました。
今後ともよろしくお願いいたします。

```html
<!DOCTYPE html>
<html lang="ja">
<head>
<meta charset="utf-8">
<title>アオナギクレープ のぼり</title>
<link rel="stylesheet" href="https://fonts.googleapis.com/css2?family=Yuji+Boku&family=Yomogi&family=Noto+Serif+JP:wght@700&display=swap">
<style>
  :root {
    --page: #ffffff;
    --cloth: #f6edd6;
    --cloth-edge: #ecdfbf;
    --ink: #1c1713;
    --ink-soft: #3a302a;
    --stamp: #c8321f;
    --stamp-text: #fbf3e1;
    --grain: #c9b48a;
    --leaf: #a4a88a;
    --tab-line: #8a8a8a;
    --logo-brown: #6b3f22;
  }
  * { margin: 0; padding: 0; box-sizing: border-box; }
  html, body {
    width: 826px; height: 1200px; overflow: hidden;
    background: var(--page);
  }
  .canvas { position: relative; width: 826px; height: 1200px; }

  .nobori-tab {
    position: absolute;
    background: var(--page);
    border: 2px solid var(--tab-line);
  }
  .nobori-tab--top { width: 26px; height: 18px; top: 24px; }
  .nobori-tab--side { width: 18px; height: 26px; left: 212px; }

  .nobori {
    position: absolute;
    left: 228px; top: 40px;
    width: 370px; height: 1110px;
    background: radial-gradient(ellipse at 50% 45%, var(--cloth) 60%, var(--cloth-edge) 100%);
    border: 1px solid #d9ccae;
    overflow: hidden;
  }

  .rice-plant {
    position: absolute;
    border-radius: 40% 40% 30% 30%;
    opacity: 0.4;
  }
  .rice-plant--upper-right {
    left: 250px; top: 130px; width: 100px; height: 300px;
    background: linear-gradient(200deg, var(--grain) 0%, var(--leaf) 80%, transparent 100%);
  }
  .rice-plant--lower-left {
    left: 0; top: 830px; width: 90px; height: 270px;
    background: linear-gradient(190deg, transparent 0%, var(--leaf) 40%, var(--grain) 100%);
  }

  .brand {
    position: absolute;
    left: 0; right: 0; top: 36px;
    display: flex; align-items: center; justify-content: center; gap: 12px;
  }
  .brand-dot {
    width: 24px; height: 24px; border-radius: 50%;
    background: var(--logo-brown);
  }
  .brand-name {
    font-family: "Yomogi", cursive;
    font-size: 44px;
    color: var(--logo-brown);
    letter-spacing: 2px;
  }

  .tagline {
    position: absolute;
    left: 66px; top: 232px;
    writing-mode: vertical-rl;
    white-space: nowrap;
    font-family: "Yomogi", cursive;
    font-size: 25px;
    line-height: 1.35;
    color: var(--ink-soft);
  }
  .tagline span { display: block; }
  .tagline .line-2 { padding-top: 20px; }
  .tagline .line-3 { padding-top: 210px; }

  .title {
    position: absolute;
    writing-mode: vertical-rl;
    font-family: "Yuji Boku", serif;
    font-weight: 400;
    color: var(--ink);
    line-height: 1;
  }
  .title--rice { left: 186px; top: 350px; font-size: 100px; letter-spacing: -4px; }
  .title--crepe { left: 92px; top: 640px; font-size: 118px; letter-spacing: -14px; }

  .origin-stamp {
    position: absolute;
    left: 282px; top: 770px;
    padding: 8px 8px;
    background: var(--stamp);
    border-radius: 3px;
    writing-mode: vertical-rl;
    white-space: nowrap;
    font-family: "Noto Serif JP", serif;
    font-weight: 700;
    font-size: 24px;
    line-height: 1.15;
    color: var(--stamp-text);
  }
  .origin-stamp span { display: block; }
  .origin-stamp .town { padding-top: 14px; }
</style>
</head>
<body>
<div class="canvas">
  <div class="nobori-tab nobori-tab--top" style="left:236px"></div>
  <div class="nobori-tab nobori-tab--top" style="left:564px"></div>
  <div class="nobori-tab nobori-tab--side" style="top:60px"></div>
  <div class="nobori-tab nobori-tab--side" style="top:330px"></div>
  <div class="nobori-tab nobori-tab--side" style="top:600px"></div>
  <div class="nobori-tab nobori-tab--side" style="top:870px"></div>
  <div class="nobori-tab nobori-tab--side" style="top:1110px"></div>

  <div class="nobori">
    <div class="rice-plant rice-plant--upper-right" role="img" aria-label="稲穂のイラスト"></div>
    <div class="rice-plant rice-plant--lower-left" role="img" aria-label="稲穂のイラスト"></div>

    <div class="brand">
      <span class="brand-dot"></span>
      <span class="brand-name">Lunelle</span>
    </div>

    <p class="tagline">
      <span class="line-1">「アオナギ」の米粉で</span>
      <span class="line-2">ことのほかおいしいクレープ</span>
      <span class="line-3">できました</span>
    </p>

    <h1 class="title title--rice">アオナギ</h1>
    <h1 class="title title--crepe">クレープ</h1>

    <div class="origin-stamp">
      <span class="prefecture">岐阜県</span>
      <span class="town">輪之内町</span>
    </div>
  </div>
</div>
</body>
</html>
```